Environmental Group Website Template

We want a website template for an environmental cause. The website should have a dark content area that is transparent. The website text and icons are white.
The background is a nature scene. The background image repeats.
Industry/Entity Type
Group

```html
<!DOCTYPE html>
<html lang="en">
<head>
<meta charset="utf-8">
<title>Verdant Reach — Environmental Group</title>
<link rel="stylesheet" href="https://fonts.googleapis.com/css2?family=Lato:wght@300;400;700;900&display=swap">
<style>
:root{
  --green:#1f8a4c;
  --green-dark:#17703c;
  --green-bright:#2fb45c;
  --white:#ffffff;
  --ink:#2b2b2b;
  --muted:#6f6f6f;
  --panel:#e3e3e3;
  --dark:#2f2f2f;
  --darker:#1c1c1c;
  --glass:rgba(20,30,40,.55);
  --track:#ffffff;
}
*{box-sizing:border-box;margin:0;padding:0}
html,body{width:1200px;height:4082px;overflow:hidden}
body{font-family:'Lato',Arial,sans-serif;color:var(--ink);background:var(--white);position:relative}
section,header,footer{position:absolute;left:0;width:1200px}
.abs{position:absolute}
.btn{display:inline-block;font-size:13px;font-weight:700;letter-spacing:1px;text-transform:uppercase;padding:12px 22px}
.btn-solid{background:var(--green);color:var(--white)}
.btn-line{border:2px solid currentColor}
.photo{position:absolute}

/* hero */
.hero{top:0;height:760px;overflow:hidden}
.hero-photo{inset:0;background:
  radial-gradient(circle at 54% 62%,#fff6d0 0,#ffc65a 6%,#f08a2a 18%,rgba(200,90,40,.0) 42%),
  linear-gradient(180deg,#5d7f95 0%,#8aa4b0 30%,#d98f55 60%,#5b4a3e 80%,#2a2722 100%)}
.hero-tree{right:0;top:0;width:520px;height:760px;background:radial-gradient(ellipse at 70% 30%,rgba(25,30,20,.9) 0,rgba(25,30,20,.75) 45%,rgba(25,30,20,0) 72%)}
.nav{top:0;left:0;width:1200px;height:130px;background:var(--green);display:flex;align-items:center;justify-content:space-between;padding:0 60px 0 150px}
.brand{display:flex;align-items:center;gap:14px;color:var(--white);font-size:26px;font-weight:700}
.brand-dot{width:44px;height:44px;border-radius:50%;background:var(--white)}
.menu{display:flex;gap:26px;align-items:center;list-style:none;color:var(--white);font-size:13px;font-weight:700;letter-spacing:.5px}
.hero-copy{left:180px;top:380px;color:var(--white)}
.hero-copy h1{font-size:56px;font-weight:700;line-height:1.12;width:680px}
.hero-copy p{font-size:14px;margin:18px 0 28px;opacity:.9}

/* about */
.about{top:770px;height:510px;overflow:hidden}
.about-photo{inset:0;background:linear-gradient(180deg,#3b78b8 0%,#8fb3d6 28%,#c9d9e3 42%,#50708a 52%,#2d4a60 75%,#6f7f88 100%)}
.about h2{position:absolute;top:60px;width:100%;text-align:center;color:var(--white);font-size:46px;font-weight:700;letter-spacing:2px}
.pillar{position:absolute;top:130px;width:300px;text-align:center;color:var(--white)}
.pillar svg{display:block;margin:0 auto}
.pillar h3{font-size:15px;font-weight:700;letter-spacing:1px;margin-top:12px}
.pillar p{background:var(--glass);font-size:13px;line-height:1.5;padding:16px 18px;margin-top:14px;text-align:left}

/* explore */
.explore{top:1285px;height:500px}
.explore-main{left:0;top:0;width:580px;height:385px;background:linear-gradient(135deg,#8fa56a 0%,#6b7f4c 40%,#b98a6a 60%,#c9c2b8 100%)}
.thumb{top:392px;width:140px;height:108px}
.explore-panel{left:585px;top:0;width:615px;height:500px;background:var(--panel);padding:60px 120px 0 24px}
.explore-panel h2{font-size:40px;font-weight:400;margin-bottom:26px}
.explore-panel p{font-size:14px;line-height:1.6;color:var(--muted);margin-bottom:18px}
.explore-panel .btn{color:var(--ink);margin-top:8px}

/* challenges */
.challenges{top:1785px;height:820px}
.section-title{position:absolute;width:100%;text-align:center;font-size:38px;font-weight:400;letter-spacing:1px;color:var(--ink)}
.quote{position:absolute;border:1px solid #d8d8d8;background:var(--white);display:flex}
.quote .text{padding:22px 24px;font-size:14px;line-height:1.55;color:var(--ink)}
.quote .photo{position:static;flex:0 0 260px}
.author{position:absolute;display:flex;align-items:center;gap:14px}
.author .name{font-size:13px;font-weight:700;text-align:right}
.author .role{font-size:11px;color:var(--muted);text-align:right}
.avatar{width:52px;height:52px;border-radius:50%;background:#9a9a9a}

/* solutions & events */
.dark{top:2620px;height:540px;background:var(--dark);color:var(--white)}
.dark h2{font-size:40px;font-weight:400;margin-bottom:30px}
.solutions{position:absolute;left:180px;top:90px;width:380px}
.solutions p{font-size:14px;line-height:1.6;margin-bottom:18px}
.events{position:absolute;left:600px;top:90px;width:420px}
.bar{margin-bottom:26px}
.bar .label{font-size:12px;margin-bottom:6px;display:flex;justify-content:space-between}
.bar .track{height:12px;background:var(--track);position:relative}
.bar .fill{position:absolute;left:0;top:0;bottom:0;background:var(--green-bright)}
.bar .pct{font-size:10px;background:var(--white);color:var(--ink);padding:1px 6px}

/* news */
.news{top:3160px;height:620px}
.post{position:absolute;top:150px;width:260px}
.post .photo{position:static;height:175px}
.post h3{font-size:17px;font-weight:900;line-height:1.3;margin:16px 0 10px}
.post .meta{font-size:11px;color:var(--muted);margin-bottom:12px}
.post p{font-size:13px;line-height:1.55;color:var(--muted)}

/* cta & footer */
.cta{top:3780px;height:125px;background:var(--green);color:var(--white)}
.cta h2{position:absolute;left:180px;top:36px;font-size:22px;font-weight:700}
.cta p{position:absolute;left:180px;top:70px;font-size:12px;opacity:.9}
.cta .btn{position:absolute;left:838px;top:40px}
.site-footer{top:3905px;height:177px;background:var(--darker);color:var(--white)}
.site-footer .brand{position:absolute;left:60px;top:60px}
.office{position:absolute;top:40px;width:200px;font-size:12px;line-height:1.6;color:#cfcfcf}
.office h4{color:var(--white);font-size:13px;font-weight:700;letter-spacing:1px;margin-bottom:8px}
</style>
</head>
<body>

<header class="hero">
  <div class="photo hero-photo" role="img" aria-label="Photo of the sun setting over hills behind a large tree"></div>
  <div class="photo hero-tree" role="img" aria-label="Silhouetted tree branches"></div>
  <nav class="nav abs">
    <div class="brand"><span class="brand-dot"></span>Verdant Reach</div>
    <ul class="menu">
      <li>HOME</li><li>ABOUT</li><li>EXPLORE</li><li>CHALLANGES</li><li>SOLUTIONS</li><li>EVENTS</li><li>NEWS</li>
      <li><svg width="16" height="16" viewBox="0 0 16 16" fill="none" stroke="#fff" stroke-width="2"><circle cx="6.5" cy="6.5" r="5"/><line x1="10" y1="10" x2="15" y2="15"/></svg></li>
    </ul>
  </nav>
  <div class="hero-copy abs">
    <h1>We're here to create your online presense and style</h1>
    <p>We build clean, open spaces for groups that care for the planet and its people.</p>
    <span class="btn btn-solid">Start today with us</span>
  </div>
</header>

<section class="about">
  <div class="photo about-photo" role="img" aria-label="Photo of a calm lake shore under a blue sky"></div>
  <h2>ABOUT</h2>
  <div class="pillar" style="left:150px">
    <svg width="150" height="120" viewBox="0 0 150 120">
      <circle cx="75" cy="60" r="56" fill="#2fb45c"/>
      <circle cx="75" cy="40" r="12" fill="#fff"/><rect x="60" y="56" width="30" height="34" rx="10" fill="#fff"/>
      <circle cx="45" cy="48" r="9" fill="#fff"/><rect x="34" y="60" width="22" height="26" rx="8" fill="#fff"/>
      <circle cx="105" cy="48" r="9" fill="#fff"/><rect x="94" y="60" width="22" height="26" rx="8" fill="#fff"/>
    </svg>
    <h3>OUR TEAM</h3>
    <p>Lorem ipsum dolor sit amet, consectetur adipiscing elit. Nam at tortor quis lorem dictum.</p>
  </div>
  <div class="pillar" style="left:450px">
    <svg width="150" height="120" viewBox="0 0 150 120">
      <circle cx="75" cy="64" r="52" fill="#2fb45c"/>
      <rect x="20" y="8" width="110" height="36" rx="18" fill="#2fb45c" stroke="#fff" stroke-width="2"/>
      <text x="75" y="32" text-anchor="middle" font-family="Lato,Arial,sans-serif" font-size="15" font-weight="700" fill="#fff">DONATE</text>
      <path d="M48 88 q10 -22 27 -12 q17 -10 27 12 z" fill="#fff"/>
    </svg>
    <h3>DONATE</h3>
    <p>Lorem ipsum dolor sit amet, consectetur adipiscing elit. Nam at tortor quis lorem dictum.</p>
  </div>
  <div class="pillar" style="left:750px">
    <svg width="150" height="120" viewBox="0 0 150 120">
      <circle cx="75" cy="60" r="56" fill="#2fb45c"/>
      <rect x="36" y="30" width="52" height="34" rx="6" fill="#fff"/><path d="M46 64 l0 12 l12 -12z" fill="#fff"/>
      <rect x="66" y="52" width="50" height="32" rx="6" fill="#fff" stroke="#2fb45c" stroke-width="3"/><path d="M104 84 l0 12 l-12 -12z" fill="#fff"/>
    </svg>
    <h3>VOLUNTEERS</h3>
    <p>Lorem ipsum dolor sit amet, consectetur adipiscing elit. Nam at tortor quis lorem dictum.</p>
  </div>
</section>

<section class="explore">
  <div class="photo explore-main" role="img" aria-label="Photo of a child drinking from an outdoor water fountain"></div>
  <div class="photo thumb" style="left:0;background:linear-gradient(135deg,#c8a48a,#6e8a5a)" role="img" aria-label="Photo of children outdoors"></div>
  <div class="photo thumb" style="left:146px;background:linear-gradient(135deg,#d9d2c6,#8ea070)" role="img" aria-label="Photo of a family in a park"></div>
  <div class="photo thumb" style="left:292px;background:linear-gradient(135deg,#a9c48a,#e4eadb)" role="img" aria-label="Photo of a child with a water bottle"></div>
  <div class="photo thumb" style="left:438px;background:linear-gradient(135deg,#7fa2c4,#c6d6a8)" role="img" aria-label="Photo of people walking by a river"></div>
  <div class="explore-panel abs">
    <h2>Explore</h2>
    <p>Lorem ipsum dolor sit amet, consectetur adipiscing elit. Nam at tortor quis lorem dictum finibus. Sed vel velit nec urna porta tempor at in nibh.</p>
    <p>Lorem ipsum dolor sit amet, consectetur adipiscing elit. Nam at tortor quis lorem dictum finibus. Sed vel velit nec urna porta tempor at in nibh.</p>
    <span class="btn btn-line">More about our team</span>
  </div>
</section>

<section class="challenges">
  <h2 class="section-title" style="top:70px">CHALLANGES</h2>

  <div class="quote" style="left:60px;top:160px;width:520px;height:230px">
    <div class="photo" style="background:linear-gradient(135deg,#6f8f4a,#b9c98c 55%,#4d6a3a)" role="img" aria-label="Photo of a volunteer working in a field"></div>
    <div class="text">Nulla consequat massa quis enim. Donec pede justo, fringilla vel, aliquet nec, vulputate eget, arcu. In enim justo, rhoncus ut, imperdiet a, venenatis vitae.</div>
  </div>
  <div class="author" style="left:330px;top:410px"><div><div class="name">Joe Doe</div><div class="role">Creative Director at Leafline.com</div></div><span class="avatar"></span></div>

  <div class="quote" style="left:600px;top:160px;width:540px;height:200px">
    <div class="text">Nulla consequat massa quis enim. Donec pede justo, fringilla vel, aliquet nec, vulputate eget, arcu. In enim justo, rhoncus ut, imperdiet a, venenatis vitae.</div>
    <div class="photo" style="flex-basis:240px;background:linear-gradient(135deg,#d9e6ef,#a7bdcc 50%,#c9a98a)" role="img" aria-label="Photo of children on a beach"></div>
  </div>
  <div class="author" style="left:600px;top:380px"><span class="avatar"></span><div><div class="name" style="text-align:left">Joe Doe</div><div class="role" style="text-align:left">Creative Director at Leafline.com</div></div></div>

  <div class="quote" style="left:180px;top:470px;width:400px;height:170px">
    <div class="text">Nulla consequat massa quis enim. Donec pede justo, fringilla vel, aliquet nec, vulputate eget, arcu. In enim justo, rhoncus ut, imperdiet a, venenatis vitae.</div>
  </div>
  <div class="author" style="left:330px;top:660px"><div><div class="name">Joe Doe</div><div class="role">Creative Director at Leafline.com</div></div><span class="avatar"></span></div>

  <div class="quote" style="left:600px;top:450px;width:400px;height:170px">
    <div class="text">Nulla consequat massa quis enim. Donec pede justo, fringilla vel, aliquet nec, vulputate eget, arcu. In enim justo, rhoncus ut, imperdiet a, venenatis vitae.</div>
  </div>
  <div class="author" style="left:600px;top:640px"><span class="avatar"></span><div><div class="name" style="text-align:left">Joe Doe</div><div class="role" style="text-align:left">Creative Director at Leafline.com</div></div></div>
</section>

<section class="dark">
  <div class="solutions">
    <h2>Solutions</h2>
    <p>Lorem ipsum dolor sit amet, consectetur adipiscing elit. Nam at tortor quis lorem dictum finibus. Sed vel velit nec urna porta tempor at in nibh.</p>
    <p>Lorem ipsum dolor sit amet, consectetur adipiscing elit. Nam at tortor quis lorem dictum finibus. Sed vel velit nec urna porta tempor at in nibh.</p>
    <span class="btn btn-line">View case studies</span>
  </div>
  <div class="events">
    <h2>Events</h2>
    <div class="bar"><div class="label"><span>Tree planting</span><span class="pct">92%</span></div><div class="track"><div class="fill" style="width:92%"></div></div></div>
    <div class="bar"><div class="label"><span>Clean water</span><span class="pct">68%</span></div><div class="track"><div class="fill" style="width:68%"></div></div></div>
    <div class="bar"><div class="label"><span>Recycling</span><span class="pct">85%</span></div><div class="track"><div class="fill" style="width:85%"></div></div></div>
    <div class="bar"><div class="label"><span>Clean energy</span><span class="pct">60%</span></div><div class="track"><div class="fill" style="width:60%"></div></div></div>
    <div class="bar"><div class="label"><span>Education</span><span class="pct">75%</span></div><div class="track"><div class="fill" style="width:75%"></div></div></div>
  </div>
</section>

<section class="news">
  <h2 class="section-title" style="top:70px">News</h2>
  <article class="post" style="left:180px">
    <div class="photo" style="background:linear-gradient(180deg,#4c7fb0,#9fc0dc 50%,#2d4a63)" role="img" aria-label="Photo of a lake at dusk"></div>
    <h3>Cache Invalidation Strategies With Fernleaf Cache</h3>
    <div class="meta">March 4, 2016 &nbsp;·&nbsp; 3 Comments</div>
    <p>Nearly ten years ago we set out to keep parks clean. This product was not built for reach but for care in every town.</p>
  </article>
  <article class="post" style="left:470px">
    <div class="photo" style="background:linear-gradient(180deg,#2c3f7a,#5e6fb0 45%,#e0a15a 60%,#1e2a40)" role="img" aria-label="Photo of a city skyline over water at night"></div>
    <h3>Cache Invalidation Strategies With Fernleaf Cache</h3>
    <div class="meta">March 4, 2016 &nbsp;·&nbsp; 3 Comments</div>
    <p>Nearly ten years ago we set out to keep parks clean. This product was not built for reach but for care in every town.</p>
  </article>
  <article class="post" style="left:740px">
    <div class="photo" style="background:linear-gradient(180deg,#6ca5d8,#b8d6ea 45%,#3f7f8f 70%,#a89a7a)" role="img" aria-label="Photo of a rocky shore with trees"></div>
    <h3>Cache Invalidation Strategies With Fernleaf Cache</h3>
    <div class="meta">March 4, 2016 &nbsp;·&nbsp; 3 Comments</div>
    <p>Nearly ten years ago we set out to keep parks clean. This product was not built for reach but for care in every town.</p>
  </article>
</section>

<section class="cta">
  <h2>Are you ready to go?</h2>
  <p>Join the group today, share your ideas and help us grow a greener place together.</p>
  <span class="btn btn-line">Start your project</span>
</section>

<footer class="site-footer">
  <div class="brand"><span class="brand-dot"></span>Verdant Reach</div>
  <div class="office" style="left:390px"><h4>NEW YORK</h4>128 Green Lane, Suite 4<br>New York, NY 10012<br>+1 555 010 2040<br>hello@verdantreach.org</div>
  <div class="office" style="left:620px"><h4>LONDON</h4>42 Meadow Road<br>London, E2 7LH<br>+44 20 5550 1020<br>london@verdantreach.org</div>
  <div class="office" style="left:850px"><h4>MADRID</h4>Calle del Olmo 18<br>28012 Madrid<br>+34 91 555 0190<br>madrid@verdantreach.org</div>
</footer>

</body>
</html>
```